Pelbrook Metal Roofing INC.

Hello,
I am working with a local business to design them a new website. The designer I had worked with moved to colorado and has taken a new job. He recommended that I try posting my new jobs on here. I would need a design and assistance setting the site up on my host nimbus server. I work by myself and handle the sales side of things and need a designer that can help me out.
This company is a metal roofing business. The current page I made for them is www.pelbrookmetalinc.example

They would like the new site to be similar to http://www.tamblecreekalloy.example

Please let me know if this is something that you could do for us.
Updates

the company wants the site to look very similar to this http://www.tamblecreekalloy.exampleis that something you could do, please get in touch with me.Thanks Added Tuesday, January 10, 2017

Industry/Entity Type

Business

Font styles to use
Sans Serif

Colors
ed252d

Requirements
Must have
• the company wants the site to look very similar to this
• http://www.tamblecreekalloy.example
• is that something you could do, please get in touch with me.
• Thanks

```html
<!DOCTYPE html>
<html lang="en">
<head>
<meta charset="utf-8">
<title>Pelbrook Metal Inc</title>
<link href="https://fonts.googleapis.com/css2?family=Jost:wght@400;500&family=Open+Sans:wght@400;600;700&display=swap" rel="stylesheet">
<style>
:root{
  --red:#ed252d;
  --ink:#222;
  --muted:#666;
  --page:#f2f2f2;
  --white:#fff;
  --line:#ddd;
}
*{box-sizing:border-box;margin:0;padding:0}
html,body{width:699px;height:1200px;overflow:hidden}
body{position:relative;background:var(--page);font-family:"Open Sans",Arial,sans-serif;color:var(--ink)}
.abs{position:absolute}
.brand{font-family:"Jost",Arial,sans-serif;color:var(--red);font-size:18px;font-weight:400;letter-spacing:.2px;white-space:nowrap}
.site-header{left:0;top:0;width:699px;height:66px;background:var(--white);box-shadow:0 1px 3px rgba(0,0,0,.08)}
.search{left:469px;top:11px;width:83px;height:18px;border:1px solid #bbb;font-size:5px;color:#888;display:flex;align-items:center;gap:4px;padding-left:7px}
.quote{left:565px;top:11px;width:57px;height:18px;border:1px solid var(--red);color:var(--red);font-size:5.5px;display:flex;align-items:center;justify-content:center}
.nav a{position:absolute;top:42px;height:16px;font-size:6px;color:var(--ink);text-decoration:none;display:flex;align-items:center;justify-content:center;text-transform:uppercase}
.nav a.active{background:var(--red);color:#fff;font-weight:600;width:38px}
.slider{left:76px;top:87px;width:545px;height:250px;background:#e4e4e4;box-shadow:0 12px 10px -8px rgba(0,0,0,.25)}
.tab{position:absolute;left:9px;width:143px;height:53px;background:#fff;border:4px solid #fff;outline:1px solid #e2e2e2;outline-offset:-5px;display:flex;align-items:center;gap:9px;padding-left:10px}
.tab h3{font-family:"Jost",sans-serif;font-weight:400;font-size:9.5px;color:#222}
.tab p{font-size:5.5px;color:#777;margin-top:3px}
.tab.on{background:var(--red);border-color:var(--red);outline-color:rgba(255,255,255,.5)}
.tab.on h3{color:#fff;font-weight:500}.tab.on p{color:#fff}
.tab.on::after{content:"";position:absolute;right:-17px;top:13px;border:13px solid transparent;border-left:13px solid var(--red)}
.hero{position:absolute;left:158px;top:7px;width:381px;height:236px;background:linear-gradient(180deg,#5ea7e8 0%,#b9d8f2 40%,#7a4a40 60%,#e9e3d8 100%)}
.hero h2{position:absolute;left:15px;top:189px;color:#fff;font-family:"Jost",sans-serif;font-weight:500;font-size:13.5px;line-height:19px;letter-spacing:.4px;text-shadow:0 1px 2px rgba(0,0,0,.4)}
.dots{position:absolute;right:0;bottom:0;width:58px;height:13px;background:#e4e4e4;display:flex;justify-content:center;align-items:center;gap:5px}
.dots i{width:4px;height:4px;border-radius:50%;background:#bbb}.dots i.on{background:var(--red)}
.section-title{left:0;width:699px;text-align:center;color:var(--red);font-family:"Jost",sans-serif;font-size:16px;font-weight:400}
.rule{left:294px;top:418px;width:111px;height:1px;background:#ddd}
.product{width:190px;text-align:center}
.product .img{width:165px;height:85px;margin:0 auto}
.product h4{margin-top:28px;font-family:"Jost",sans-serif;font-weight:400;font-size:9.5px;line-height:15px;text-transform:uppercase}
.product p{margin-top:10px;font-size:5.8px;line-height:12px;color:#555;text-transform:uppercase}
.product .more{display:inline-block;margin-top:14px;width:59px;height:18px;line-height:16px;border:1px solid var(--red);color:var(--red);font-size:5.8px;text-transform:uppercase}
.subscribe{left:76px;top:733px;width:545px;height:191px;background:linear-gradient(180deg,#e9e9e9,#dcdcdc)}
.subscribe::before{content:"";position:absolute;left:264px;top:0;border:9px solid transparent;border-top:9px solid var(--page)}
.subscribe h2{position:absolute;top:42px;width:100%;text-align:center;color:var(--red);font-family:"Jost",sans-serif;font-weight:400;font-size:15px}
.subscribe p{position:absolute;top:74px;width:100%;text-align:center;font-size:8px;font-weight:400;color:#444}
.field{position:absolute;left:87px;top:115px;width:373px;height:34px;background:#f7f7f7;box-shadow:0 1px 3px rgba(0,0,0,.15);display:flex;align-items:center;padding-left:13px;gap:8px;font-size:6px;color:#444}
.signup{position:absolute;right:6px;top:4px;width:59px;height:25px;background:var(--red);color:#fff;font-weight:700;font-size:9px;display:flex;align-items:center;justify-content:center}
.footer{left:0;top:978px;width:699px;height:222px;background:#fff}
.f-head{font-family:"Jost",sans-serif;font-size:7px;text-transform:uppercase;color:#111}
.small{font-size:6px;color:#555}
.social i{position:absolute;top:1087px;width:16px;height:16px;border-radius:50%;background:var(--red)}
.menu li{list-style:none;height:13px;font-size:6px;color:#555}
.hours{font-size:6px;color:#555}.hours b{position:absolute;left:40px;font-weight:600;color:#222;white-space:nowrap}
.ico{width:14px;height:14px;border:1px solid #ccc;border-radius:50%;display:inline-flex;align-items:center;justify-content:center;vertical-align:middle;margin-right:9px}
</style>
</head>
<body>
<header class="abs site-header">
  <div class="abs brand" style="left:76px;top:21px">PELBROOK METAL INC</div>
  <div class="abs search"><svg width="5" height="5" viewBox="0 0 10 10"><circle cx="4" cy="4" r="3" fill="none" stroke="#666" stroke-width="1.5"/><path d="M6.5 6.5L9 9" stroke="#666" stroke-width="1.5"/></svg>SEARCH</div>
  <div class="abs quote">GET A QUOTE</div>
  <nav class="nav">
    <a class="active" style="left:310px">Home</a>
    <a style="left:367px">About Us</a>
    <a style="left:425px">Projects</a>
    <a style="left:481px">News</a>
    <a style="left:524px">Products</a>
    <a style="left:582px">Contact Us</a>
  </nav>
</header>

<section class="abs slider">
  <div class="tab" style="top:7px">
    <svg width="14" height="12" viewBox="0 0 14 12"><path d="M1 1h5l1 1 1-1h5v10H8l-1 1-1-1H1z" fill="none" stroke="#555" stroke-width=".8"/><path d="M7 2v9" stroke="#555" stroke-width=".8"/></svg>
    <div><h3>Featured Products</h3><p>Our Latest Products here</p></div></div>
  <div class="tab on" style="top:68px">
    <svg width="16" height="14" viewBox="0 0 16 14"><path d="M1 7L8 1l7 6M3 6v7h10V6" fill="none" stroke="#fff" stroke-width="1"/><rect x="6" y="8" width="4" height="5" fill="none" stroke="#fff"/></svg>
    <div><h3>Residential</h3><p>Home.Garge</p></div></div>
  <div class="tab" style="top:128px">
    <svg width="14" height="16" viewBox="0 0 14 16"><rect x="2" y="1" width="10" height="14" fill="none" stroke="#555" stroke-width=".8"/><path d="M4 4h2v2H4zM8 4h2v2H8zM4 8h2v2H4zM8 8h2v2H8z" fill="none" stroke="#555" stroke-width=".6"/></svg>
    <div><h3>Commercial</h3><p>Lorem Ipsum is simply</p></div></div>
  <div class="tab" style="top:188px">
    <svg width="16" height="14" viewBox="0 0 16 14"><path d="M1 6L8 1l7 5M3 5v8h10V5M6 13V8h4v5" fill="none" stroke="#555" stroke-width=".8"/></svg>
    <div><h3>Agriculture</h3><p>Lorem Ipsum is simply</p></div></div>
  <div class="hero" role="img" aria-label="Photo of a house with a red metal tile roof against a blue sky">
    <h2>MANUFACTURERS OF QUALITY<br>BUILDING COMPONENTS</h2>
    <div class="dots"><i></i><i></i><i class="on"></i><i></i><i></i></div>
  </div>
</section>

<h2 class="abs section-title" style="top:384px">OUR PRODUCTS</h2>
<div class="abs rule"></div>

<article class="abs product" style="left:63px;top:447px">
  <div class="img" role="img" aria-label="Red metal roof tile panel" style="background:linear-gradient(180deg,#b1333a,#7a1a20)"></div>
  <h4>Residential<br>Metal Roofing</h4>
  <p>Ribbed, standing seam and a variety of<br>metal roofing options.</p>
  <span class="more">Read More</span>
</article>
<article class="abs product" style="left:258px;top:447px">
  <div class="img" role="img" aria-label="Silver corrugated steel panel" style="width:140px;background:linear-gradient(90deg,#e0e0e0,#b8b8b8,#eee,#aaa,#ddd)"></div>
  <h4>Commercial and<br>Agricultural Applications</h4>
  <p>28 Gauge panels are the thickest<br>and strongest in the industry.</p>
  <span class="more">Read More</span>
</article>
<article class="abs product" style="left:452px;top:447px">
  <div class="img" role="img" aria-label="Wooden post frame building structure" style="width:115px;background:linear-gradient(180deg,#f0dca0,#d6b870)"></div>
  <h4>Complete Post Frame<br>Building Packages</h4>
  <p>28 Gauge panels are the thickest<br>and strongest in the industry.</p>
  <span class="more">Read More</span>
</article>

<section class="abs subscribe" role="img" aria-label="Light grey corrugated metal background">
  <h2>SUBSCRIBE</h2>
  <p>Sign up to hear from us about specials, sales, and events.</p>
  <div class="field">
    <svg width="8" height="6" viewBox="0 0 8 6"><rect x=".5" y=".5" width="7" height="5" fill="none" stroke="#777" stroke-width=".7"/><path d="M.5.5L4 3.5 7.5.5" fill="none" stroke="#777" stroke-width=".7"/></svg>
    <span>E mail Address</span>
    <div class="signup">SIGNUP</div>
  </div>
</section>

<footer class="abs footer"></footer>
<div class="abs brand" style="left:76px;top:1017px">PELBROOK METAL INC</div>
<div class="abs f-head" style="left:143px;top:1065px;font-size:6px">Follow Us</div>
<div class="social"><i style="left:129px"></i><i style="left:154px"></i><i style="left:180px"></i></div>

<div class="abs f-head" style="left:297px;top:1019px">Contact Us</div>
<div class="abs small" style="left:296px;top:1045px"><span class="ico"><svg width="6" height="6" viewBox="0 0 10 10"><path d="M2 1l2 2-1 1.5c.8 1.5 1.5 2.2 3 3L7.5 6l2 2-1.5 1.5C4.5 9 1 5.5.5 2.5z" fill="#999"/></svg></span>555-014-0765</div>
<div class="abs small" style="left:296px;top:1070px"><span class="ico"><svg width="6" height="6" viewBox="0 0 10 10"><rect x="1" y="4" width="8" height="4" fill="none" stroke="#999"/><rect x="3" y="1" width="4" height="3" fill="none" stroke="#999"/></svg></span>555-014-4931</div>

<div class="abs f-head" style="left:426px;top:1019px">Menu</div>
<ul class="abs menu" style="left:427px;top:1042px">
  <li>Home</li><li>About us</li><li>Projects</li><li>Products</li><li>News</li><li>Contact Us</li>
</ul>

<div class="abs f-head" style="left:524px;top:1019px">Hours</div>
<div class="abs hours" style="left:525px;top:1046px">Monday :<b>Friday: 7am - 5pm</b></div>
<div class="abs hours" style="left:525px;top:1064px">Saturday :<b>7AM-12PM</b></div>
<div class="abs hours" style="left:525px;top:1084px">Sunday :<b>CLOSED</b></div>

<div class="abs" style="left:76px;top:1147px;width:545px;height:1px;background:var(--line)"></div>
<div class="abs small" style="left:0;top:1168px;width:699px;text-align:center">Copyrights @ 2017 All Rights Reserved</div>
</body>
</html>
```